business cards for heating company

I need business cards for my heating air conditioning and chimney company located in upstate NY I would like for them to be colorful and catchy on heavy stock with preferably a glossy finish on front of card but the ability to write something on one half of the back with maybe some bullets on the other half of the back I also need to be able to change the name and title of employees on the card and also incorporate some of our current look and feel from our trucks and website I also want to be able to use this design or similar to have door hangers made lawn signs coffee mugs key chains etc. our website is Brindlecove.com

Target Market(s)

homeowners

Industry/Entity Type

Air Conditioning

Contact Information for Business Card

should have website brindlecove.com , phone number 585-437-9168 please look at website for ideas

Font styles to use
Sans Serif

Colors
ec1f27
3176b5
fbee3f

Requirements
Must have
• a complete look
Nice to have
• a discount offer like 10% military and first responders
• senior discount %5

```html
<!DOCTYPE html>
<html lang="en">
<head>
<meta charset="utf-8">
<title>Brindle Cove – Business Card</title>
<link rel="stylesheet" href="https://fonts.googleapis.com/css2?family=Montserrat:wght@400;500;800&display=swap">
<style>
  :root {
    --magenta: #c8175d;
    --blue: #1f55d6;
    --white: #ffffff;
    --paper: #f4f4f4;
    --ink-soft: #fbe3ec;
    --backdrop: #e6e4e1;
  }
  * { margin: 0; padding: 0; box-sizing: border-box; }
  html, body { width: 1200px; height: 899px; overflow: hidden; }
  body {
    background: var(--backdrop);
    font-family: "Montserrat", Arial, sans-serif;
    display: flex; align-items: center; justify-content: center;
  }
  .card {
    position: relative;
    width: 1000px; height: 571px;
    border-radius: 48px;
    overflow: hidden;
    background: linear-gradient(160deg, var(--white), var(--paper));
    box-shadow: 0 14px 40px rgba(0,0,0,.18);
  }
  .card__shape { position: absolute; inset: 0; }
  .brand {
    position: absolute; left: 50px; top: 170px;
  }
  .brand__name {
    display: inline-block;
    font-weight: 800; font-size: 52px; letter-spacing: 1px;
    color: var(--magenta); line-height: 1;
  }
  .brand__tagline {
    margin-top: 8px;
    font-weight: 500; font-size: 25px; letter-spacing: .5px;
    color: var(--blue);
  }
  .details {
    position: absolute; left: 615px; top: 70px;
    color: var(--white);
  }
  .details__name { font-weight: 500; font-size: 25px; letter-spacing: 1px; }
  .details__title { font-size: 17px; color: var(--ink-soft); margin-top: 4px; }
  .details__address { font-size: 20px; line-height: 1.4; margin-top: 78px; }
  .contact { list-style: none; margin-top: 72px; }
  .contact li {
    display: flex; align-items: center; gap: 14px;
    font-size: 16px; letter-spacing: 1px; height: 33px;
  }
  .contact svg { width: 18px; height: 18px; fill: none; stroke: var(--white); stroke-width: 2; }
</style>
</head>
<body>
  <article class="card">
    <svg class="card__shape" viewBox="0 0 1000 571" preserveAspectRatio="none" aria-hidden="true">
      <path d="M548 0 C640 120 625 420 70 571 C610 440 620 130 565 0 Z" fill="var(--blue)"/>
      <path d="M570 0 C650 130 630 430 90 571 L1000 571 L1000 0 Z" fill="var(--magenta)"/>
    </svg>

    <div class="brand">
      <span class="brand__name">BRINDLE COVE</span>
      <p class="brand__tagline">HEATING, COOLING &amp; CHIMNEY</p>
    </div>

    <div class="details">
      <p class="details__name">MARK DELANEY</p>
      <p class="details__title">Managing Director</p>
      <p class="details__address">214 Orchard Hill Road,<br>Rochester NY</p>
      <ul class="contact">
        <li><svg viewBox="0 0 24 24"><path d="M5 3h4l2 5-3 2a12 12 0 0 0 6 6l2-3 5 2v4a2 2 0 0 1-2 2A17 17 0 0 1 3 5a2 2 0 0 1 2-2z"/></svg>585-437-9168</li>
        <li><svg viewBox="0 0 24 24"><rect x="7" y="2" width="10" height="20" rx="2"/><path d="M11 18h2"/></svg>585-437-9168</li>
        <li><svg viewBox="0 0 24 24"><rect x="3" y="9" width="18" height="10" rx="2"/><path d="M7 9V4h10v5"/></svg>585-437-9168</li>
        <li><svg viewBox="0 0 24 24"><rect x="3" y="5" width="18" height="14" rx="2"/><path d="M3 7l9 6 9-6"/></svg>info@brindlecove.com</li>
        <li><svg viewBox="0 0 24 24"><circle cx="12" cy="12" r="9"/><path d="M3 12h18M12 3c3 3 3 15 0 18M12 3c-3 3-3 15 0 18"/></svg>www.brindlecove.com</li>
      </ul>
    </div>
  </article>
</body>
</html>
```